Homepage Real Estate Agency

I need a web design for a real estate agency in Luxembourg. A short draft for the front page can be found in the project details. (Page 1+2) The main colors of the site should be blue as shown in the project details. (Page 3)
The main target for this site is to promote real estates and a small presentation of the company.

Industry/Entity Type

Real Estate

Requirements
Must have
• On the front page estates are shown in a short preview in small boxes, on the right side is a search. The search is hidden except for the front page. The header has 4 buttons and the logo of the company.

```html
<!DOCTYPE html>
<html lang="en">
<head>
<meta charset="utf-8">
<title>Moselle Habitat — Real Estate</title>
<link rel="stylesheet" href="https://fonts.googleapis.com/css2?family=Roboto+Condensed:wght@400;700&family=PT+Sans:wght@400;700&display=swap">
<style>
:root{
  --navy:#1f2a7a;
  --deep:#020a4a;
  --royal:#0d4fc0;
  --red:#a3000a;
  --deal-red:#c4120d;
  --ink:#3a3a3a;
  --muted:#666;
  --rule:#c9c9c9;
  --card:#f3f3f3;
  --card-line:#d6d6d6;
  --slate:#3f5873;
  --slate-light:#7b94ad;
  --sky:#9cc4e4;
  --white:#fff;
}
*{box-sizing:border-box;margin:0;padding:0}
html,body{width:1024px;height:1200px;overflow:hidden}
body{
  position:relative;
  font-family:"PT Sans",sans-serif;
  color:var(--ink);
  background:
    radial-gradient(ellipse 600px 260px at 120px 40px,rgba(70,150,255,.55),transparent 70%),
    radial-gradient(ellipse 380px 500px at 1024px 620px,rgba(40,120,230,.5),transparent 70%),
    linear-gradient(170deg,#0a3fa8 0%,#06237a 35%,var(--deep) 75%);
}
.page{
  position:absolute;left:62px;top:27px;width:900px;height:1130px;
  background:var(--white);border-radius:12px;
}
.abs{position:absolute}

/* header */
.header-line{left:15px;top:49px;width:870px;height:1px;background:var(--navy)}
.header-band{left:15px;top:53px;width:870px;height:32px;background:linear-gradient(#fff,#ececec)}
.header-bar{left:15px;top:85px;width:870px;height:4px;background:var(--red)}
.brand{left:40px;top:48px;display:flex;align-items:center;gap:8px;background:var(--white);padding:0 10px 0 6px;height:38px}
.brand-dot{width:16px;height:16px;border-radius:50%;background:var(--navy)}
.brand-name{font-family:"Roboto Condensed",sans-serif;font-size:20px;font-weight:700;color:var(--navy)}
.main-nav{right:15px;top:53px;display:flex;height:29px}
.main-nav a{
  font-family:"Roboto Condensed",sans-serif;font-size:16px;color:var(--navy);
  text-decoration:none;padding:0 10px;line-height:29px;border-left:1px solid #d4d4d4;
}
.main-nav a:first-child{border-left:none;color:var(--red)}

.hero{left:15px;top:119px;width:870px;height:314px;
  background:linear-gradient(180deg,#8db8e8 0%,#c9dcec 35%,#c7ad84 60%,#6f7d4a 88%,#4c5c34 100%)}

/* left column */
.section-title{font-family:"Roboto Condensed",sans-serif;font-size:16px;color:var(--ink);display:flex;align-items:center;gap:6px}
.section-title em{font-style:normal;color:var(--navy)}
.section-title svg{width:14px;height:14px}
.intro{left:15px;top:479px;width:562px;font-size:12.5px;line-height:18px;color:var(--muted);text-align:justify}
.intro-rule{left:15px;top:531px;width:562px;height:1px;background:var(--rule)}

.deal{width:274px;height:208px;background:var(--card);border:1px solid var(--card-line)}
.deal-photo{position:absolute;left:10px;top:10px;width:252px;height:103px;
  background:linear-gradient(180deg,#6e8f55 0%,#b7bcc4 40%,#e5e7ea 70%,#5e7a3c 100%)}
.deal-text{position:absolute;left:9px;top:119px;width:254px;font-size:12.5px;line-height:18px;color:var(--muted);text-align:justify}
.deal-btn{position:absolute;right:10px;top:177px;height:25px;padding:0 8px 0 6px;background:var(--white);
  border:1px solid #ccc;font-size:11.5px;color:var(--deal-red);display:flex;align-items:center;gap:6px}
.deal-btn::before{content:"";border-left:4px solid var(--deal-red);border-top:3px solid transparent;border-bottom:3px solid transparent}

/* search */
.search{left:591px;top:447px;width:294px;height:240px;border:1px solid #dcdcdc;background:var(--white)}
.search-head{height:36px;background:#ededed;font-family:"Roboto Condensed",sans-serif;font-size:16px;color:var(--navy);padding:8px 16px}
.field{position:absolute;left:19px;width:253px;height:23px;border:1px solid #d2d2d2;font-size:12px;color:#aaa;padding:3px 8px}
.search-label{position:absolute;left:19px;top:137px;font-size:12px;color:var(--muted)}
.select-arrow{position:absolute;right:3px;top:4px;width:13px;height:13px;background:linear-gradient(#dce7fb,#a7bde8);border:1px solid #8fa6d6;border-radius:2px}
.find-btn{position:absolute;left:209px;top:198px;width:63px;height:23px;background:linear-gradient(#e2e2e2,#bdbdbd);border:1px solid #b3b3b3;font-size:12px;color:#666;text-align:center;line-height:21px}

.services{left:593px;top:701px;width:292px;height:185px;background:linear-gradient(120deg,var(--slate) 0%,#4f6a86 55%,var(--slate-light) 100%)}
.services h3{position:absolute;left:19px;top:10px;font-family:"Roboto Condensed",sans-serif;font-weight:400;font-size:16px;color:var(--white);padding-bottom:4px;border-bottom:1px solid #9fb2c6;width:124px}
.services ul{position:absolute;left:21px;top:57px;list-style:none}
.services li{font-size:12.5px;color:var(--white);line-height:20px;display:flex;align-items:center;gap:9px}
.services li::before{content:"";border-left:4px solid var(--white);border-top:3px solid transparent;border-bottom:3px solid transparent}

.contact{left:592px;top:901px;width:293px;height:100px;background:linear-gradient(180deg,#eef5fb 0%,#cfe1f1 45%,var(--sky) 100%)}
.contact-art{position:absolute;left:16px;top:16px;width:70px;height:66px;background:linear-gradient(135deg,#c6d9ea,#e6eff7)}
.contact-title{position:absolute;left:110px;top:13px;font-family:"Roboto Condensed",sans-serif;font-size:16px;color:#3a4350}
.contact-sub{position:absolute;left:111px;top:33px;font-size:11px;color:var(--white);letter-spacing:.3px}
.contact-phone{position:absolute;left:104px;top:64px;font-family:"Roboto Condensed",sans-serif;font-size:21px;color:#3a4350}

/* footer */
.footer-rule{left:15px;top:1030px;width:870px;height:8px;background:radial-gradient(ellipse at top,#d2d2d2 0%,transparent 70%)}
.footer-nav{right:15px;top:1064px;font-size:12.5px;color:var(--ink);text-align:right;line-height:20px}
.footer-nav a{color:var(--ink);text-decoration:none}
</style>
</head>
<body>
<div class="page">
  <div class="abs header-line"></div>
  <div class="abs header-band"></div>
  <div class="abs header-bar"></div>
  <div class="abs brand"><span class="brand-dot"></span><span class="brand-name">Moselle Habitat</span></div>
  <nav class="abs main-nav">
    <a href="#">A Vendre</a><a href="#">Construction</a><a href="#">Locations</a><a href="#">Chercons</a>
  </nav>

  <div class="abs hero" role="img" aria-label="Photo of a detached family house with a garage under a blue sky"></div>

  <h2 class="abs section-title" style="left:15px;top:445px">
    <svg viewBox="0 0 14 14"><rect x="0.5" y="0.5" width="13" height="13" rx="2" fill="none" stroke="#555"/><path d="M3 7h6M6.5 4l3 3-3 3" fill="none" stroke="#555" stroke-width="1.6"/></svg>
    Welcome to <em>Moselle Habitat</em>
  </h2>
  <p class="abs intro">Bellevue Property Group is recognized as a preferred supplier of various types and makes of imported and indigenous Electrical, Electronic Spares for Imported machinery, Industrial Switchgears.</p>
  <div class="abs intro-rule"></div>

  <h2 class="abs section-title" style="left:15px;top:542px">
    <svg viewBox="0 0 14 14"><rect x="0.5" y="0.5" width="13" height="13" rx="2" fill="none" stroke="#555"/><path d="M3 7h6M6.5 4l3 3-3 3" fill="none" stroke="#555" stroke-width="1.6"/></svg>
    Our Deals <em>and Prices</em>
  </h2>

  <article class="abs deal" style="left:16px;top:572px">
    <div class="deal-photo" role="img" aria-label="Photo of a two-storey house with a porch"></div>
    <p class="deal-text">some text will come here some text will come here some text will come here some text will come here some text will come here some text</p>
    <a class="deal-btn">Check Deal</a>
  </article>
  <article class="abs deal" style="left:303px;top:572px">
    <div class="deal-photo" role="img" aria-label="Photo of a two-storey house with a porch"></div>
    <p class="deal-text">some text will come here some text will come here some text will come here some text will come here some text will come here some text</p>
    <a class="deal-btn">Check Deal</a>
  </article>
  <article class="abs deal" style="left:15px;top:793px">
    <div class="deal-photo" role="img" aria-label="Photo of a two-storey house with a porch"></div>
    <p class="deal-text">some text will come here some text will come here some text will come here some text will come here some text will come here some text</p>
    <a class="deal-btn">Check Deal</a>
  </article>
  <article class="abs deal" style="left:303px;top:793px">
    <div class="deal-photo" role="img" aria-label="Photo of a two-storey house with a porch"></div>
    <p class="deal-text">some text will come here some text will come here some text will come here some text will come here some text will come here some text</p>
    <a class="deal-btn">Check Deal</a>
  </article>

  <aside class="abs search">
    <div class="search-head">Search</div>
    <div class="field" style="top:56px">Search by Keyword</div>
    <div class="field" style="top:86px">City, State</div>
    <div class="search-label">Sort by Price</div>
    <div class="field" style="top:159px">~ Select your Price ~<span class="select-arrow"></span></div>
    <div class="find-btn">Find</div>
  </aside>

  <aside class="abs services">
    <h3>Our Services</h3>
    <ul>
      <li>Service No. 1</li><li>Service No. 2</li><li>Service No. 3</li><li>Service No. 4</li><li>Service No. 5</li>
    </ul>
  </aside>

  <aside class="abs contact">
    <div class="contact-art" role="img" aria-label="Line drawing of two profiles facing each other"></div>
    <div class="contact-title">GET IN TOUCH</div>
    <div class="contact-sub">CUSTOMER CENTER</div>
    <div class="contact-phone">+352 2745-8190</div>
  </aside>

  <div class="abs footer-rule"></div>
  <div class="abs footer-nav">
    <a href="#">A Vendre</a> | <a href="#">Construction</a> | <a href="#">Locations</a> | <a href="#">Chercons</a><br>
    © 2012 Moselle Habitat. All Rights Reserved.
  </div>
</div>
</body>
</html>
```